Marrowgate Auctions Business Cards Design Needed

I need a business card design that is modern looking - double sided (maybe just my logo on the back, but open to suggestions) - the overall design is up to you. I want it to be easy to read - not over the top flashy. I already have a company logo which I uploaded so that needs to be used. The colors of my logo are the colors I want on the card... so blue and gray (do need to match the logo colors).

Requirements
Must have
• Would like the card to be sleek, modern and easy to ready

```html
<!DOCTYPE html>
<html lang="en">
<head>
<meta charset="utf-8">
<title>Marrowgate Auctions – Business Cards</title>
<link href="https://fonts.googleapis.com/css2?family=Roboto:wght@400;700&display=swap" rel="stylesheet">
<style>
  :root {
    --brand-blue: #2f84ee;
    --brand-gray: #3f4a52;
    --line-blue: #2a6fb8;
    --stage: #eaebed;
    --card: #ffffff;
  }
  * { margin: 0; padding: 0; box-sizing: border-box; }
  html, body { width: 1200px; height: 1200px; overflow: hidden; }
  body {
    background: var(--stage);
    font-family: "Roboto", Arial, sans-serif;
    position: relative;
  }
  .card {
    position: absolute;
    background: var(--card);
  }
  .card--front { left: 123px; top: 37px; width: 954px; height: 545px; }
  .card--back  { left: 122px; top: 621px; width: 956px; height: 547px; }

  .brand-square {
    position: absolute;
    background: var(--brand-blue);
  }
  .card--front .brand-square { left: 397px; top: 38px; width: 170px; height: 170px; }
  .card--back .brand-square  { left: 376px; top: 46px; width: 206px; height: 206px; }

  .brand-name {
    position: absolute;
    left: 0; right: 0;
    text-align: center;
    font-weight: 700;
    color: var(--brand-gray);
    text-transform: uppercase;
    white-space: nowrap;
    line-height: 1;
  }
  .card--front .brand-name { top: 232px; font-size: 51px; letter-spacing: 1px; }
  .card--back .brand-name  { top: 306px; font-size: 66px; letter-spacing: 2px; }

  .person {
    position: absolute;
    right: 37px;
    top: 340px;
    text-align: right;
  }
  .person__name {
    font-size: 38px;
    color: var(--brand-blue);
    line-height: 1.1;
    letter-spacing: 0.5px;
  }
  .person__title {
    font-size: 28px;
    color: var(--brand-gray);
    line-height: 1.2;
    letter-spacing: 0.6px;
  }
  .divider {
    position: absolute;
    left: 33px;
    top: 406px;
    width: 460px;
    height: 2px;
    background: var(--line-blue);
  }
  .contact {
    position: absolute;
    left: 33px;
    top: 425px;
    list-style: none;
  }
  .contact li {
    display: flex;
    align-items: center;
    height: 29px;
    font-size: 24px;
    color: var(--brand-gray);
    letter-spacing: 0.4px;
  }
  .contact svg { width: 20px; height: 20px; margin-right: 11px; flex: none; }

  .tagline {
    position: absolute;
    left: 0; right: 0;
    top: 460px;
    text-align: center;
    font-size: 36px;
    letter-spacing: 1px;
    color: var(--brand-gray);
    white-space: nowrap;
  }
  .tagline__accent { color: var(--brand-blue); }
</style>
</head>
<body>
  <section class="card card--front">
    <div class="brand-square"></div>
    <div class="brand-name">Marrowgate Auctions</div>

    <div class="person">
      <div class="person__name">Glen Harrow</div>
      <div class="person__title">Owner/President - Auctioneer</div>
    </div>
    <div class="divider"></div>

    <ul class="contact">
      <li>
        <svg viewBox="0 0 24 24" aria-hidden="true"><path fill="var(--brand-blue)" d="M6.6 10.8a15 15 0 0 0 6.6 6.6l2.2-2.2a1 1 0 0 1 1-.25 11.4 11.4 0 0 0 3.6.57 1 1 0 0 1 1 1V20a1 1 0 0 1-1 1A17 17 0 0 1 3 4a1 1 0 0 1 1-1h3.5a1 1 0 0 1 1 1c0 1.25.2 2.45.57 3.57a1 1 0 0 1-.25 1z"/><path fill="none" stroke="var(--brand-blue)" stroke-width="1.8" d="M14 3a7 7 0 0 1 7 7M14 6.5a3.5 3.5 0 0 1 3.5 3.5"/></svg>
        555-014-2287
      </li>
      <li>
        <svg viewBox="0 0 24 24" aria-hidden="true"><rect x="2" y="5" width="20" height="14" fill="none" stroke="var(--brand-blue)" stroke-width="2"/><path d="M2 5l10 8 10-8M2 19l7-7M22 19l-7-7" fill="none" stroke="var(--brand-blue)" stroke-width="2"/></svg>
        marrowgatebids@mailhub.com
      </li>
      <li>
        <svg viewBox="0 0 24 24" aria-hidden="true"><circle cx="12" cy="12" r="10" fill="none" stroke="var(--brand-blue)" stroke-width="2"/><path d="M2 12h20M12 2c3 3 3 17 0 20M12 2c-3 3-3 17 0 20" fill="none" stroke="var(--brand-blue)" stroke-width="1.6"/></svg>
        bidrevive.com
      </li>
    </ul>
  </section>

  <section class="card card--back">
    <div class="brand-square"></div>
    <div class="brand-name">Marrowgate Auctions</div>
    <p class="tagline"><span class="tagline__accent">Improving Charity</span> Auctions Nationwide</p>
  </section>
</body>
</html>
```